Ridgefield Tournament

Tennis Tournament Poster - Size 11 X 17 inches

Volley Crown Metro Classic
April 4th - 7th, 2013
Briarvale Country Club & Holloway Tennis Center
Two Different Age Divisions for all levels - 18 up & 45 up
Men's, Women's, & Mixed - Singles and Doubles
All Levels - 2.5-Open
Non QRTA player welcomed
www.VolleyCrown.example
Updates

Need to change one thing and add another....

Two different age divisions for all divisions

should be

Two different age divisions for all levels

Also... need to add to the poster

Non QRTA players Welcomed

Industry/Entity Type

Club

Requirements
Nice to have
• Would like to have a place in the middle of the poster where I can attached kind of like a stack of sticky notes in the shape of a tennis ball and people can take one. So it would be nice if there was an image on the poster in the shape and size of a ball, preferable close to the middle for me to attach those.

```html
<!DOCTYPE html>
<html lang="en">
<head>
<meta charset="utf-8">
<title>Volley Crown Metro Classic</title>
<link href="https://fonts.googleapis.com/css2?family=Cabin:ital,wght@0,400;0,500;0,600;0,700;1,700&family=Marcellus&display=swap" rel="stylesheet">
<style>
  :root {
    --bg-dark: #27302c;
    --bg-mid: #36413c;
    --band: #c6c7a9;
    --ink-dark: #27302c;
    --venue-green: #cfe2c2;
    --white: #ffffff;
    --muted: #a9ab8f;
    --division: #cac8aa;
    --court-line: rgba(255,255,255,0.14);
    --ball-light: #9cd64a;
    --ball-dark: #4f8a1c;
  }
  * { margin: 0; padding: 0; box-sizing: border-box; }
  html, body { width: 783px; height: 1200px; overflow: hidden; background: var(--bg-dark); }
  .poster {
    position: relative;
    width: 783px;
    height: 1200px;
    overflow: hidden;
    background: radial-gradient(ellipse at 70% 45%, var(--bg-mid) 0%, var(--bg-dark) 70%);
    font-family: "Cabin", sans-serif;
  }
  .court-lines { position: absolute; inset: 0; }
  .brand {
    position: absolute; top: 52px; left: 0; width: 100%;
    text-align: center;
    font-weight: 700; font-size: 74px; letter-spacing: 1px;
    color: var(--white); text-transform: uppercase;
  }
  .rule {
    position: absolute; left: 0; width: 100%;
    border-top: 2px dashed rgba(255,255,255,0.75);
  }
  .rule--top { top: 180px; }
  .rule--bottom { top: 354px; }
  .title-band {
    position: absolute; top: 188px; left: 0; width: 100%; height: 158px;
    background: var(--band);
    text-align: center; color: var(--ink-dark);
    font-style: italic; font-weight: 700;
  }
  .title-band .title-main { display: block; font-size: 58px; line-height: 1; padding-top: 24px; letter-spacing: 1px; }
  .title-band .title-sub { display: block; font-size: 48px; line-height: 1; padding-top: 14px; }
  .text { position: absolute; left: 43px; white-space: nowrap; }
  .date {
    left: 0; width: 100%; text-align: center; top: 380px;
    font-size: 60px; font-weight: 700; color: var(--white);
  }
  .date sup { font-size: 30px; vertical-align: 0; }
  .venue { font-size: 41px; color: var(--venue-green); font-weight: 500; }
  .venue--one { top: 472px; }
  .venue--two { top: 526px; }
  .detail { font-size: 30px; color: var(--white); font-weight: 500; }
  .detail--divisions { top: 590px; }
  .detail--levels { top: 638px; }
  .ages { top: 690px; font-family: "Marcellus", serif; font-size: 54px; color: var(--division); }
  .detail--events { top: 771px; }
  .formats { top: 826px; font-size: 48px; line-height: 58px; color: var(--venue-green); font-weight: 500; }
  .welcome { top: 957px; font-size: 24px; color: var(--muted); }
  .detail--range { top: 1000px; }
  .ball-art { position: absolute; left: 450px; top: 716px; width: 440px; height: 440px; }
  .web-band {
    position: absolute; left: 0; top: 1064px; width: 484px; height: 67px;
    background: var(--band);
    color: var(--ink-dark); font-size: 32px; font-weight: 600;
    line-height: 67px; padding-left: 43px;
  }
</style>
</head>
<body>
<div class="poster">
  <svg class="court-lines" width="783" height="1200" aria-hidden="true">
    <line x1="0" y1="405" x2="490" y2="775" stroke="var(--court-line)" stroke-width="12"/>
    <line x1="783" y1="425" x2="0" y2="1000" stroke="var(--court-line)" stroke-width="12"/>
  </svg>

  <div class="brand">Volley Crown</div>

  <div class="rule rule--top"></div>
  <div class="title-band">
    <span class="title-main">VOLLEY CROWN METRO</span>
    <span class="title-sub">Classic</span>
  </div>
  <div class="rule rule--bottom"></div>

  <div class="text date">April 4<sup>th</sup> - 7<sup>th</sup>, 2013</div>
  <div class="text venue venue--one">Briarvale Country Club &amp;</div>
  <div class="text venue venue--two">Holloway Tennis Center</div>
  <div class="text detail detail--divisions">Two Different Age Divisions</div>
  <div class="text detail detail--levels">for all Levels -</div>
  <div class="text ages">18 up &amp; 45 up</div>
  <div class="text detail detail--events">Men's, Women's, &amp; Mixed</div>
  <div class="text formats">Singles and<br>Doubles</div>
  <div class="text welcome">Non QRTA Players Welcomed</div>
  <div class="text detail detail--range">All Levels - 2.5-Open</div>

  <svg class="ball-art" viewBox="0 0 440 440" role="img" aria-label="Illustration of a grassy green tennis ball, spot for a tear-off note pad">
    <defs>
      <radialGradient id="ballFill" cx="40%" cy="35%" r="70%">
        <stop offset="0%" stop-color="var(--ball-light)"/>
        <stop offset="100%" stop-color="var(--ball-dark)"/>
      </radialGradient>
    </defs>
    <circle cx="220" cy="220" r="218" fill="url(#ballFill)"/>
  </svg>

  <div class="web-band">www.VolleyCrown.example</div>
</div>
</body>
</html>
```